Postcard Mailer

We are a pizza pub that is the only local restaurant that offers and delivers pizza, burgers, salads and wings.

We just opened and want to send out a postcard to the community. thinking on one side a nice design with pics etc. then on the back a list of our daily food and drink specials.

Industry/Entity Type

Restaurant

Colors
eb1f27

```html
<!DOCTYPE html>
<html lang="en">
<head>
<meta charset="utf-8">
<title>Mabel and Marco – Postcard Mailer</title>
<link rel="stylesheet" href="https://fonts.googleapis.com/css2?family=Black+Ops+One&family=Nunito:wght@800&display=swap">
<style>
  :root {
    --canvas: #efd9cc;
    --wood-light: #c48a55;
    --wood-mid: #9b6232;
    --wood-dark: #6e3f1c;
    --crust: #d9a866;
    --sauce: #b8452c;
    --topping-green: #4f8a2c;
    --accent-green: #93c852;
    --ink-white: #ffffff;
    --ink-black: #151210;
    --brand-red: #eb1f27;
  }
  * { box-sizing: border-box; margin: 0; padding: 0; }
  html, body { width: 1200px; height: 609px; overflow: hidden; }
  body { background: var(--canvas); position: relative; font-family: "Black Ops One", system-ui, sans-serif; }

  .postcard {
    position: absolute;
    width: 518px; height: 403px;
    overflow: hidden;
    box-shadow: 3px 4px 8px rgba(60, 35, 20, .35);
  }
  .postcard--front { left: 48px; top: 43px; }
  .postcard--back { left: 617px; top: 125px; }

  .wood-backdrop {
    position: absolute; inset: 0;
    background:
      radial-gradient(ellipse at 20% 10%, rgba(255,240,220,.45), transparent 55%),
      repeating-linear-gradient(90deg, transparent 0 68px, rgba(60,30,10,.35) 68px 71px),
      linear-gradient(180deg, var(--wood-light), var(--wood-mid) 60%, var(--wood-dark));
  }

  .pizza-photo {
    position: absolute;
    left: 228px; top: 34px;
    width: 500px; height: 500px;
    border-radius: 50%;
    background: radial-gradient(circle at 40% 45%, var(--sauce) 0%, #c9573a 35%, var(--topping-green) 52%, #b5623a 62%, var(--crust) 70%, #c99456 74%);
  }

  .headline {
    position: absolute;
    color: var(--accent-green);
    line-height: 1;
    letter-spacing: .5px;
  }
  .postcard--front .headline { left: 182px; top: 22px; font-size: 27px; }
  .postcard--back .headline { left: 26px; top: 20px; font-size: 42px; }

  .brand-mark {
    position: absolute;
    display: flex; flex-direction: column; align-items: center;
    text-align: center;
  }
  .brand-mark__circle { border-radius: 50%; }
  .brand-mark__name { line-height: 1.05; }
  .brand-mark__city { font-size: 10px; margin-top: 6px; }

  .postcard--front .brand-mark { left: 46px; top: 206px; width: 150px; color: var(--ink-white); }
  .postcard--front .brand-mark__circle { width: 52px; height: 52px; background: var(--ink-white); margin-bottom: 8px; }
  .postcard--front .brand-mark__name { font-size: 15px; }

  .postcard--back .brand-mark { left: 296px; top: 104px; width: 190px; color: var(--ink-black); }
  .postcard--back .brand-mark__circle { width: 92px; height: 92px; background: var(--ink-black); margin-bottom: 10px; }
  .postcard--back .brand-mark__name { font-size: 18px; }
  .postcard--back .brand-mark__city { font-size: 11px; }

  .phone {
    position: absolute;
    display: flex; align-items: center; gap: 6px;
    font-family: "Nunito", system-ui, sans-serif;
    font-weight: 800;
    color: var(--accent-green);
    line-height: 1;
  }
  .phone svg { fill: var(--accent-green); }
  .postcard--front .phone { left: 14px; top: 357px; font-size: 27px; }
  .postcard--back .phone { left: 258px; top: 346px; font-size: 29px; }

  .menu { position: absolute; left: 28px; top: 138px; color: var(--ink-black); }
  .menu__title { font-size: 18px; margin-bottom: 22px; }
  .menu__list { list-style: none; font-size: 21px; line-height: 27px; }
</style>
</head>
<body>

<section class="postcard postcard--front">
  <div class="wood-backdrop" role="img" aria-label="Photo of a rustic wooden table dusted with flour, with a rolling pin"></div>
  <div class="pizza-photo" role="img" aria-label="Photo of a supreme pizza topped with tomatoes, peppers, onions and olives"></div>
  <h1 class="headline">BURGERS AND PIZZA</h1>
  <div class="brand-mark">
    <span class="brand-mark__circle"></span>
    <span class="brand-mark__name">MABEL AND MARCO</span>
    <span class="brand-mark__city">SEAPORT, NC</span>
  </div>
  <div class="phone">
    <svg width="22" height="26" viewBox="0 0 24 24" aria-hidden="true"><path d="M6.6 10.8a15.1 15.1 0 0 0 6.6 6.6l2.2-2.2a1 1 0 0 1 1-.25 11.4 11.4 0 0 0 3.6.57 1 1 0 0 1 1 1V20a1 1 0 0 1-1 1A17 17 0 0 1 3 4a1 1 0 0 1 1-1h3.5a1 1 0 0 1 1 1c0 1.25.2 2.45.57 3.57a1 1 0 0 1-.25 1z"/></svg>
    <span>910.555 0142</span>
  </div>
</section>

<section class="postcard postcard--back">
  <div class="wood-backdrop" role="img" aria-label="Photo of a rustic wooden table dusted with flour, with a rolling pin"></div>
  <h2 class="headline">PIZZA PUB</h2>
  <div class="menu">
    <p class="menu__title">MENU</p>
    <ul class="menu__list">
      <li>APPETIZERS</li>
      <li>GOURMET SALADS</li>
      <li>BUILD YOUR OWN PIZZA</li>
      <li>SPECIALTY PIZZA</li>
      <li>TOPPINGS</li>
    </ul>
  </div>
  <div class="brand-mark">
    <span class="brand-mark__circle"></span>
    <span class="brand-mark__name">MABEL AND MARCO</span>
    <span class="brand-mark__city">SEAPORT, NC</span>
  </div>
  <div class="phone">
    <svg width="24" height="28" viewBox="0 0 24 24" aria-hidden="true"><path d="M6.6 10.8a15.1 15.1 0 0 0 6.6 6.6l2.2-2.2a1 1 0 0 1 1-.25 11.4 11.4 0 0 0 3.6.57 1 1 0 0 1 1 1V20a1 1 0 0 1-1 1A17 17 0 0 1 3 4a1 1 0 0 1 1-1h3.5a1 1 0 0 1 1 1c0 1.25.2 2.45.57 3.57a1 1 0 0 1-.25 1z"/></svg>
    <span>910.555 0142</span>
  </div>
</section>

</body>
</html>
```